UI design for an Zevo(Tulafon) photo editing app

This design contest is to design the UI/screenshots of an Zevo(Tulafon) app named "Vivid Pane". Some minor design details are left out at this point as the mockup is still in progress. The icon of this app will be designed separately. The winner of this job will be selected to work on a long term basis as an Tulaslate version and several updates will have to be designed as well as the Korvanix version. Please take
this as a long term opportunity.
The photo app is called "Vivid Pane". The design need to dynamic, different that stands out WITH a serious and polished look.
All the mockups and sample screenshots are attached for ease. Please thoroughly review them.
This app has the following screens:
1. Welcome screen(just a simple background will do now as icon will be put later).
2. Main Screen (or LightBox)
The background of this screen can be the same as the background of the welcome screen. It can be a wooden background OR a background of your
choice that fits and blends in the buttons and fonts/colors.
The main screen has this bars/buttons/options that has separate screens:
On top, menu bar:
has these buttons
settings on the left(icon)
in the middle, 3 buttons (please check lightbox mockup and lightbox sample pics)
on the right, share icon(check share screen sample)
Our share options:
"Share" button screenshot:
Our share options:
Save
Email
Copy
Plimsee
Nodlyne
Snapu
Chirrup
in the middle, just background where the pictures would appear later after importing
or saving
at the bottom bar:
3 buttons:
Camera Roll(on the left)
Camera Button(middle)
Advanced Button(on the right)
2 versions of this screenshot need to be designed.
1. regular version with all the options
2. regular version plus the "steam effect" button showing up on top of the "Advanced" button(mockup with red lines)
3 separate screenshots need to be designed for the options"
settings screenshot(please check sample):
Gift Vivid Pane to a friend
Rate/review in the Bazo Mart
(space in between...so they are grouped)
Geotagiing(on/off)
Captured photos get location-specific information(these lines in smaller fonts)
Launch in Capture Mode(on/off)
Vivid Pane is automatically lauched in camera mode
Autosave to Camera Roll(on/off)
Captured photos are directly saved to camera roll
Reset All Tutorials
Tap to reset all the tutorials
In the "Steam Effect" screen, please check the mockup
Top Bar: lightbox button(to go back), heading and Done button
Middle: Steam background(provided)
Bottom bar:
refresh button
droplets(when clicked on/off options show up on top, please check mockup)
finger size(when clicked 3 options show up)
steam density(when clicked 3 options show up)
Please use the buttons for the droplets, finger size and steam density from the steam effects button image provided)
(and also the background of this screenshot(in the middle) would be a steam screen which is provided. Please use the
steam background provided and you need to use the background in the middle, just omit the top and the bottom bar from the image)
Now back to the main(lightbox screen):
When Clicked on the "Camera" in the middle of the bottom bar, the capture mode screen shows up.
Please refer to the mockup first
There you will see the cancel button on the left
camera button in the middle
a small settings button on the right
and a filters button on the right
and the filters bar on the top
ours need to like this
please refer to capture mode sample 1
please refer to capture mode sample 2
please refer to capture mode sample 3
normal
Grid
timer(5/15/30 secs)
Edit Screen(check sample)
Edit options
Adjust:(displayed on a bar)
1. Left
2. Right
3. Horizontal
4. Vertical
5. Straightening
Crop:
None
Original
Golden
Freeform
Square
3:2
4:3
4:6
5:7
8:10
16:9
Filters:(please note that this filter icon and the filter icon in the "capture mode" screenshot need to same)
(the filters are displayed on a bar, please check sample)
There is a sample picture that you need to put in the picture of the filters. It would be same picture in
every filter at this point.
00.None
0.Calibrate
1. aurora
2. drizzle
3. icicle
4. blizzard
5. calm
6. dew
7. knot
8. dry
9. eye
10. flurry
11. fog
12. frost
13. hail
14. haze
15. heat
16. humid
17. overcast
18. polar
19. thermal
20. trace
Editing options on top:(check sample)
Brightness
Contrast
Saturation
Textures:(dispalyed on a bar, check sample)
1.None
2.Bark
3.Grunge1
4.Grunge2
5.grunge3
6.Grunge4
7.Paper
8.Cardboard
9.Wood
10.Bokeh
11.Bricks
12.Metal
13.Asphalt
14.Pavement1
15.Pavement2
16.Paint1
17.Paint2
18.Rust
19.Towel
20.Stone1
21.Stone2
22.Wall
23.Urban1
24.Urban2
25.Urban3
26.Watercolor
Tilt-shift/Vignette:(check sample)
Borders:(check samples, at this point, we are working on them, you just need to make a bar that displays them)
1.None
2.
3.
4.
5.
6.
7.
8.
9.
10.
11.
12.
13.
14.
15.
16.
This is our primary design mockup. Upon selecting the final version, we will be working on some more and minor details(as
we are also working with the coders).
And there is a folder callled "app sample". Please take a look at it and think how our app can be different and stand out.
Thanks and feel free to contact me anytime if you have any questions. Looking forward to hearing from you and building a long term
relationship.
All camera app users who likes to edit their photos with cool tools.
Building

```html
<!DOCTYPE html>
<html lang="en">
<head>
<meta charset="utf-8">
<title>Vivid Pane – Share Sheet</title>
<link rel="stylesheet" href="https://fonts.googleapis.com/css2?family=Source+Sans+3:wght@400;600;700&display=swap">
<style>
  :root {
    --status-bg: #050505;
    --status-text: #e8e8e8;
    --nav-bg: #0e5a5c;
    --nav-edge: #0a4446;
    --nav-btn: #0c4c4e;
    --nav-btn-edge: #083638;
    --seg-bg: #b9b9b9;
    --seg-edge: #8c8c8c;
    --seg-icon: #333;
    --canvas-bg: #5c8c8a;
    --hero-fill: #1e4a4d;
    --logo: #1a5d61;
    --sheet-top: #3d3d3d;
    --sheet-mid: #333333;
    --sheet-bot: #393939;
    --rule: #262626;
    --tile: #1f1f1f;
    --tile-text: #4a4a4a;
    --label: #f2f2f2;
    --muted: #5e5e5e;
    --track: #151515;
  }
  * { box-sizing: border-box; margin: 0; padding: 0; }
  html, body { width: 800px; height: 1200px; overflow: hidden; background: var(--canvas-bg); }
  body { font-family: "Source Sans 3", "Helvetica Neue", Arial, sans-serif; position: relative; }

  .status-bar { position: absolute; left: 0; top: 0; width: 800px; height: 50px; background: var(--status-bg); color: var(--status-text); }
  .status-bar .time { position: absolute; left: 0; right: 0; top: 4px; text-align: center; font-size: 32px; font-weight: 700; }
  .status-bar svg { position: absolute; }

  .nav-bar { position: absolute; left: 0; top: 50px; width: 800px; height: 110px; background: var(--nav-bg); border-bottom: 2px solid var(--nav-edge); }
  .nav-button { position: absolute; top: 20px; width: 93px; height: 69px; background: var(--nav-btn); border: 2px solid var(--nav-btn-edge); border-radius: 8px; display: flex; align-items: center; justify-content: center; }
  .nav-button.settings { left: 17px; }
  .nav-button.add-person { left: 690px; }
  .segmented { position: absolute; left: 235px; top: 20px; width: 330px; height: 70px; background: var(--seg-bg); border: 2px solid var(--seg-edge); border-radius: 8px; display: flex; }
  .segment { flex: 0 0 110px; display: flex; align-items: center; justify-content: center; border-right: 2px solid var(--seg-edge); }
  .segment:last-child { border-right: none; font-weight: 700; font-size: 21px; color: var(--seg-icon); }

  .hero-art { position: absolute; left: 200px; top: 272px; width: 400px; height: 400px; border-radius: 50%; background: var(--hero-fill); }
  .wordmark { position: absolute; left: 0; right: 0; top: 712px; text-align: center; font-size: 62px; font-weight: 700; color: var(--logo); }

  .sheet { position: absolute; left: 0; top: 697px; width: 800px; height: 503px; }
  .sheet svg.tabs { position: absolute; left: 0; top: 0; }
  .action { position: absolute; top: 14px; width: 220px; text-align: center; color: var(--label); font-size: 36px; font-weight: 700; line-height: 1.2; }
  .action .icon { display: block; margin: 0 auto 6px; height: 50px; }
  .action.save { left: 24px; }
  .action.copy { left: 290px; }
  .action.cancel { left: 556px; }

  .share-row { position: absolute; left: 0; top: 147px; width: 800px; height: 121px; background: var(--sheet-mid); border-top: 2px solid var(--rule); border-bottom: 2px solid var(--rule); }
  .share-tile { position: absolute; top: 22px; width: 72px; height: 72px; background: var(--tile); border-radius: 12px; color: var(--tile-text); font-size: 15px; font-weight: 700; line-height: 1.1; display: flex; align-items: center; justify-content: center; text-align: center; }

  .resolution-panel { position: absolute; left: 0; top: 268px; width: 800px; height: 235px; background: var(--sheet-bot); }
  .resolution { position: absolute; left: 0; right: 0; top: 24px; text-align: center; color: #e6e6e6; font-size: 35px; font-weight: 700; }
  .slider-track { position: absolute; left: 24px; top: 106px; width: 730px; height: 24px; background: var(--track); border-radius: 12px; box-shadow: inset 0 2px 3px #000; }
  .slider-knob { position: absolute; left: 720px; top: 89px; width: 56px; height: 56px; border-radius: 50%; background: radial-gradient(circle at 40% 35%, #ffffff, #c9c9c9 45%, #8a8a8a 100%); box-shadow: 0 2px 4px #000; }
  .slider-label { position: absolute; top: 160px; color: var(--muted); font-size: 28px; font-weight: 700; }
  .slider-label.left { left: 26px; }
  .slider-label.right { right: 26px; }
</style>
</head>
<body>
  <header class="status-bar">
    <svg width="60" height="30" style="left:10px;top:10px"><polygon points="0,28 55,28 55,0" fill="#e8e8e8"/></svg>
    <div class="time">14:06 PM</div>
    <svg width="30" height="30" style="left:688px;top:10px"><circle cx="15" cy="15" r="12" fill="#e8e8e8"/><path d="M15 7v8h6" stroke="#050505" stroke-width="3" fill="none"/></svg>
    <svg width="56" height="30" style="left:732px;top:10px"><rect x="1" y="3" width="46" height="24" rx="3" fill="none" stroke="#e8e8e8" stroke-width="3"/><rect x="6" y="8" width="20" height="14" fill="#e8e8e8"/><rect x="49" y="10" width="5" height="10" fill="#e8e8e8"/></svg>
  </header>

  <nav class="nav-bar">
    <div class="nav-button settings">
      <svg width="42" height="42" viewBox="0 0 42 42"><circle cx="21" cy="21" r="13" fill="none" stroke="#bfbfbf" stroke-width="8" stroke-dasharray="5 3.2"/><circle cx="21" cy="21" r="10" fill="#bfbfbf"/><circle cx="21" cy="21" r="5" fill="#0c4c4e"/></svg>
    </div>
    <div class="segmented">
      <div class="segment"><svg width="44" height="44"><rect x="0" y="0" width="20" height="20" rx="3" fill="#333"/><rect x="24" y="0" width="20" height="20" rx="3" fill="#333"/><rect x="0" y="24" width="20" height="20" rx="3" fill="#333"/><rect x="24" y="24" width="20" height="20" rx="3" fill="#333"/></svg></div>
      <div class="segment"><svg width="44" height="44"><rect width="44" height="44" rx="4" fill="#333"/></svg></div>
      <div class="segment">Select All</div>
    </div>
    <div class="nav-button add-person">
      <svg width="56" height="46" viewBox="0 0 56 46"><circle cx="20" cy="16" r="10" fill="#bfbfbf"/><path d="M2 44c0-12 8-17 18-17s18 5 18 17z" fill="#bfbfbf"/><path d="M44 2v16M36 10h16" stroke="#bfbfbf" stroke-width="4"/></svg>
    </div>
  </nav>

  <div class="hero-art" role="img" aria-label="Camera lens illustration placeholder"></div>
  <div class="wordmark">Vivid Pane</div>

  <section class="sheet">
    <svg class="tabs" width="800" height="150">
      <path d="M0 59 L24 59 C30 -8 238 -8 244 59 L290 59 C296 -8 504 -8 510 59 L556 59 C562 -8 770 -8 776 59 L800 59 L800 150 L0 150 Z" fill="#3d3d3d" stroke="#262626" stroke-width="2"/>
    </svg>
    <div class="action save"><svg class="icon" width="50" height="50"><rect x="3" y="3" width="44" height="44" rx="3" fill="none" stroke="#1e1e1e" stroke-width="3"/></svg>Save</div>
    <div class="action copy"><svg class="icon" width="50" height="50"><rect x="0" y="14" width="34" height="34" rx="3" fill="#1e1e1e"/><rect x="14" y="0" width="34" height="34" rx="3" fill="#1e1e1e" stroke="#3d3d3d" stroke-width="3"/></svg>Copy</div>
    <div class="action cancel"><svg class="icon" width="50" height="50"><path d="M14 12L36 38M36 12L14 38" stroke="#1e1e1e" stroke-width="5"/></svg>Cancel</div>

    <div class="share-row">
      <div class="share-tile" style="left:23px">Chirrup</div>
      <div class="share-tile" style="left:138px">Nodlyne</div>
      <div class="share-tile" style="left:250px">Snapu</div>
      <div class="share-tile" style="left:364px">Stakko</div>
      <div class="share-tile" style="left:476px">Plimsee</div>
      <div class="share-tile" style="left:589px"><svg width="44" height="32"><rect x="1" y="1" width="42" height="30" rx="3" fill="#4a4a4a"/><path d="M2 3L22 18L42 3" stroke="#1f1f1f" stroke-width="3" fill="none"/></svg></div>
      <div class="share-tile" style="left:702px;font-size:19px">Other<br>Apps</div>
    </div>

    <div class="resolution-panel">
      <div class="resolution">Resolution: 3264 x 3264</div>
      <div class="slider-track"></div>
      <div class="slider-knob"></div>
      <div class="slider-label left">Share / Email</div>
      <div class="slider-label right">Save / Print</div>
    </div>
  </section>
</body>
</html>
```